Corporate Brochure for trade show in the Video Surveillance industry

We need a design for this brochure: https://files.example-share.net/s/7qkv2mpl9xw4tz/edits_Qelvora%20Deck%20%28Sept%202022%29.pptx
Print size: regular 8.5x11 inches, horizontal, number of pages depend on the design.
Need clean and corporate look , similar to this style: https://slides.example-docs.net/p/8RmtQw2LsXa4NbVc7YdKpZeHuJ3fG6oTrWiEn5Bx/edit#slide=id.h4821ccb7aef_2_31

Target Market(s)

Security integrators and monitoring stations

Industry/Entity Type

security and video surveillance

Font styles to use
Sans Serif

Colors
00AB8E
00BBA5
67D7C9
C6EFE9
E9F9F6

Requirements
Must have
• print -ready file in the end and editable file in Photoshop

```html
<!DOCTYPE html>
<html lang="en">
<head>
<meta charset="utf-8">
<title>Qelvora Brochure Spread – Alarm Station &amp; Whitelabel</title>
<link href="https://fonts.googleapis.com/css2?family=Catamaran:wght@400;500;600;700;800&display=swap" rel="stylesheet">
<style>
  :root{
    --bg:#d9d9d9;
    --paper:#f7f7f7;
    --paper-right:#fafafa;
    --teal:#1fab8e;
    --ink:#2b2b2b;
    --navy:#1f2a4a;
    --white:#ffffff;
    --grad:linear-gradient(100deg,#21b394 0%,#3aa89c 40%,#6a82b4 75%,#8456ad 100%);
  }
  *{box-sizing:border-box;margin:0;padding:0}
  html,body{width:1200px;height:641px;overflow:hidden;background:var(--bg)}
  body{font-family:"Catamaran",sans-serif;position:relative}
  .spread{position:absolute;left:30px;top:102px;width:1140px;height:437px;box-shadow:0 18px 40px rgba(0,0,0,.18)}
  .page{position:absolute;top:0;height:100%;overflow:hidden}
  .page--left{left:0;width:551px;background:var(--paper)}
  .page--right{left:551px;width:589px;background:var(--paper-right);border-left:1px solid #e2e2e2}
  .title{position:absolute;left:96px;top:44px;font-size:19px;line-height:24px;font-weight:800;letter-spacing:.5px;color:var(--teal)}
  .body-col{position:absolute;top:76px;width:203px;font-size:7.6px;line-height:12.4px;color:var(--ink);text-align:justify;letter-spacing:.15px}
  .body-col--a{left:96px}
  .body-col--b{left:312px}
  .callout{position:absolute;left:95px;top:235px;width:202px;height:154px;background:var(--grad);padding:10px 16px 0 16px;color:var(--white);font-size:7.4px;line-height:13.5px;letter-spacing:.25px}
  .callout p{text-align:justify}
  .callout-notch{position:absolute;left:120px;top:219px}
  .monitor-photo{position:absolute;left:310px;top:221px;width:241px;height:169px;background:linear-gradient(160deg,#f2f2f2 0%,#d7d7d7 55%,#3a3e45 100%)}
  .integrations{position:absolute;left:316px;top:229px;width:58px;height:119px;background:var(--white);border:1px solid #3a4a7a}
  .integrations-head{background:#3f5f87;color:var(--white);font-size:5.2px;line-height:6.4px;text-align:center;padding:3px 2px}
  .integrations ul{list-style:none;text-align:center;padding-top:6px}
  .integrations li{font-size:6.6px;font-weight:700;color:var(--navy);line-height:17px}
  .devices-blob{position:absolute;left:-16px;top:-62px}
  .devices-photo{position:absolute;left:45px;top:32px;width:235px;height:119px;background:linear-gradient(135deg,#4a5158 0%,#8a9096 50%,#2b2f34 100%);border-radius:4px}
  .whitelabel-box{position:absolute;left:40px;top:168px;width:253px;height:206px;background:var(--grad);padding:14px 18px 0 19px}
  .whitelabel-box h2{font-size:11px;font-weight:700;color:var(--navy);letter-spacing:.3px;margin-bottom:5px}
  .whitelabel-box p{font-size:7.6px;line-height:13.1px;color:var(--white);text-align:justify;letter-spacing:.25px}
  .hero-circle{position:absolute;left:301px;top:36px}
  .hero-kicker{position:absolute;left:340px;top:56px;width:130px;text-align:center;color:var(--white);font-size:10px;line-height:12px;letter-spacing:.6px}
  .hero-title{position:absolute;left:326px;top:86px;width:160px;text-align:center;color:var(--white);font-size:21px;line-height:26px;font-weight:800;letter-spacing:1px}
  .tablet-photo{position:absolute;left:350px;top:134px;width:186px;height:176px;background:linear-gradient(150deg,#2e2a28 0%,#7d6a55 45%,#b9a892 70%,#1f1f22 100%);border-radius:8px;transform:rotate(-10deg) skewX(-4deg);border:4px solid #111}
</style>
</head>
<body>
<main class="spread">
  <section class="page page--left">
    <h1 class="title">ALARM STATION</h1>
    <p class="body-col body-col--a">Included with the Qelvora platform is a web-based real-time event monitoring application for video verification. Unify multi-site and brand surveillance, extend cloud analytics to filter only accurate events and enable agents to take action on event pop-ups. This is an opportunity to use any computer as a powerful real-time monitoring device, maximize the efficiency of agents viewing only relevant events while minimizing fatigue, and leveraging object detection analytics to remove false alarms. A black screen, with any number of tiles, shown with real-time video clips of preconfigured</p>
    <p class="body-col body-col--b">video analytics rules with options available to talk-down, view camera location, screenshot, clip and share events, categorize the event type or simply acknowledge and log the event with or without a note. All camera event history is logged and searchable by event types in the admin portal. Incorporate IoT integration with webhooks to automate workflows and create triggers based on logged video event categories (e.g. trigger the gate to open, dispatch security or call the fire department with one click based on the preset acknowledged event type).</p>

    <svg class="callout-notch" width="20" height="17" viewBox="0 0 20 17" aria-hidden="true"><polygon points="10,0 20,17 0,17" fill="#23b295"/></svg>
    <div class="callout">
      <p>The Qelvora API system can also be integrated into systems such as sensors, Trevlink, Zolvane, Access Control, PoS devices, Smart TV to form an extremely efficient intelligent surveillance system.</p>
      <p>The Qelvora API system can also be integrated into systems such as sensors, Trevlink, Zolvane, Access Control, PoS devices, Smart TV to form an extremely efficient intelligent surveillance system.</p>
    </div>

    <div class="monitor-photo" role="img" aria-label="Desktop monitor on a desk showing the alarm station video wall, with keyboard and mouse"></div>
    <div class="integrations">
      <div class="integrations-head">Alarm Monitoring Software Integrations</div>
      <ul>
        <li>Brelmont</li>
        <li>Quaston</li>
        <li>Velmarq</li>
        <li>Torvexa</li>
        <li>Plindor</li>
      </ul>
    </div>
  </section>

  <section class="page page--right">
    <svg class="devices-blob" width="140" height="140" viewBox="0 0 140 140" aria-hidden="true">
      <defs><linearGradient id="blobGrad" x1="0" y1="0" x2="1" y2="0"><stop offset="0" stop-color="#1fb192"/><stop offset=".6" stop-color="#4aa59f"/><stop offset="1" stop-color="#8456ad"/></linearGradient></defs>
      <circle cx="80" cy="70" r="66" fill="url(#blobGrad)"/>
    </svg>
    <div class="devices-photo" role="img" aria-label="Laptop, desktop, tablet and phone showing the video management dashboard"></div>

    <div class="whitelabel-box">
      <h2>COMPLETE WHITE LABELLING</h2>
      <p>Qelvora is available as a white label service to customize branding of all aspects of the platform, including the mobile apps. Co-branded support is included to customize all web portals with unique sub-domains, color scheme and logos at no additional cost. But the complete rebranding removes all mention of “Qelvora,” and includes further portal style customization, branded Pellar and Drovin apps hosted in your own app stores, branded emails, SSL certificate for web portals, Kestrova JS web components and widgets for further customization opportunities of your own VMS platform. Compare the options.</p>
    </div>

    <svg class="hero-circle" width="290" height="400" viewBox="0 0 290 400" aria-hidden="true">
      <defs><linearGradient id="heroGrad" x1="0" y1="0" x2="1" y2="0"><stop offset="0" stop-color="#2bbd9c"/><stop offset=".55" stop-color="#4e8eae"/><stop offset="1" stop-color="#7f4ead"/></linearGradient></defs>
      <circle cx="104" cy="104" r="104" fill="url(#heroGrad)"/>
      <circle cx="0" cy="274" r="18" fill="#2ab89a"/>
      <circle cx="221" cy="300" r="40" fill="#2ab89a"/>
    </svg>
    <p class="hero-kicker">Professional<br>CLoud VMS:</p>
    <p class="hero-title">WHITELABEL</p>
    <div class="tablet-photo" role="img" aria-label="Tablet showing a branded video surveillance app with live camera feeds and timeline"></div>
  </section>
</main>
</body>
</html>
```